Design some Business Cards for Kelvara

A startup company named Kelvara IT is looking for a business card design. It needs to be modern, with a strong sense of professionalism and creativity. Design would need to be both front and back. No costs will be spared during printing, so incorporate any printing styles, embossing etc. Size needs to be the standard card size.

The design needs to incorporate the logo provided, include phone number, email address, job title, and company website.

Company website is [login to view URL]

Cards would be for:

Miles Harrow
CEO
Miles@kelvara-mail.example
555-402-3391

Pat Lowry
COO/CIO
Pat@kelvara-mail.example
555-739-1046

Tom Vallerup
V.P. of Design
Tom@kelvara-mail.example
555-158-6627

Dana Whitby
V.P. of Sales
Dana@kelvara-mail.example
555-823-9570

```html
<!DOCTYPE html>
<html lang="en">
<head>
<meta charset="utf-8">
<title>Kelvara IT — Business Card</title>
<link href="https://fonts.googleapis.com/css2?family=Open+Sans:wght@400;600;700&display=swap" rel="stylesheet">
<style>
  :root {
    --backdrop: #bcbdc0;
    --charcoal: #3c3c40;
    --paper: #ffffff;
    --accent: #1ba5de;
    --ink: #3c3c40;
  }
  html, body {
    margin: 0;
    padding: 0;
    overflow: hidden;
  }
  .canvas {
    position: relative;
    width: 1200px;
    height: 839px;
    background: var(--backdrop);
    font-family: "Open Sans", Arial, sans-serif;
    overflow: hidden;
  }
  .card {
    position: absolute;
    top: 104px;
    width: 408px;
    height: 631px;
    border-radius: 24px;
    overflow: hidden;
  }
  .card--front {
    left: 157px;
    background: var(--charcoal);
  }
  .card--back {
    left: 635px;
    background: var(--paper);
  }
  /* Front: brand band */
  .brand-band {
    position: absolute;
    left: 110px;
    top: 395px;
    width: 298px;
    height: 53px;
    background: var(--paper);
  }
  .brand-dot {
    position: absolute;
    left: 83px;
    top: 390px;
    width: 58px;
    height: 58px;
    border-radius: 50%;
    background: var(--paper);
    border: 4px solid var(--charcoal);
    box-sizing: content-box;
    margin-left: -4px;
    margin-top: -2px;
  }
  .brand-name {
    position: absolute;
    left: 152px;
    top: 392px;
    height: 60px;
    line-height: 60px;
    font-size: 40px;
    font-weight: 700;
    color: var(--ink);
    letter-spacing: -0.5px;
    white-space: nowrap;
  }
  .front-url {
    position: absolute;
    right: 30px;
    top: 462px;
    font-size: 18px;
    font-weight: 600;
    color: var(--paper);
    white-space: nowrap;
  }
  /* Back: person details */
  .name-tab {
    position: absolute;
    left: 0;
    top: 393px;
    width: 61px;
    height: 59px;
    background: var(--accent);
    border-radius: 0 30px 30px 0;
  }
  .person {
    position: absolute;
    left: 80px;
    top: 405px;
  }
  .person__name {
    margin: 0;
    font-size: 25px;
    font-weight: 700;
    color: var(--ink);
    line-height: 1.1;
  }
  .person__role {
    margin: 3px 0 0;
    font-size: 20px;
    font-weight: 400;
    color: var(--ink);
    line-height: 1.2;
  }
  .contact-list {
    position: absolute;
    left: 82px;
    top: 497px;
    margin: 0;
    padding: 0;
    list-style: none;
  }
  .contact-list li {
    display: flex;
    align-items: center;
    height: 32px;
    font-size: 19px;
    color: var(--ink);
  }
  .contact-list svg {
    width: 13px;
    height: 13px;
    margin-right: 14px;
    flex: none;
  }
</style>
</head>
<body>
<div class="canvas">
  <section class="card card--front" aria-label="Card front">
    <div class="brand-band"></div>
    <div class="brand-dot"></div>
    <div class="brand-name">Kelvara IT</div>
    <div class="front-url">www.kelvara-it.example</div>
  </section>

  <section class="card card--back" aria-label="Card back">
    <div class="name-tab"></div>
    <div class="person">
      <p class="person__name">Miles Harrow</p>
      <p class="person__role">CEO</p>
    </div>
    <ul class="contact-list">
      <li>
        <svg viewBox="0 0 16 16" aria-hidden="true"><path fill="#3c3c40" d="M2 5c0-2 2-3 6-3s6 1 6 3v1h-3V5H5v1H2zM4 7h8l2 6H2z"/><circle cx="8" cy="10" r="1.6" fill="#fff"/></svg>
        555-402-3391
      </li>
      <li>
        <svg viewBox="0 0 16 16" aria-hidden="true"><rect x="1" y="3" width="14" height="10" fill="#3c3c40"/><path d="M1.5 3.5L8 9l6.5-5.5" fill="none" stroke="#fff" stroke-width="1.4"/></svg>
        Miles@kelvara-mail.example
      </li>
      <li>
        <svg viewBox="0 0 16 16" aria-hidden="true"><circle cx="8" cy="8" r="6.5" fill="#3c3c40"/><path d="M1.5 8h13M8 1.5v13M8 1.5c-3 3.5-3 9.5 0 13M8 1.5c3 3.5 3 9.5 0 13" fill="none" stroke="#fff" stroke-width="1"/></svg>
        www.kelvara-it.example
      </li>
    </ul>
  </section>
</div>
</body>
</html>
```